Book cover design for modern bagpipe music book

This music book will be A4 in size and requires a design for the front and back cover. The focus is on creating a modern and eye catching design, breaking away from the stereotypes of what people think of when they think of bagpipes. Think the OPPOSITE of a bagpiper in a full kilt standing on top of a mountain playing Copper Lanterns Rising!

Book title: Rise Hum March Rest

Other front cover text : Music for the bagpipes by Dermot Fairley

Front cover file ideas uploaded

2 pictures of bagpipes attached.

- The real set of bagpipes give an idea of the correct finer details

- The toy bagpipes perhaps have a better shape with the left 'stick' down

Back cover - No real brief. Keen for it not to be a full block single colour though.

Design requires 3mm bleed for print

Open to ideas and suggestions! Thank you!

```html
<!DOCTYPE html>
<html lang="en">
<head>
<meta charset="utf-8">
<title>Rise Hum March Rest — Music for the Bagpipes</title>
<link rel="stylesheet" href="https://fonts.googleapis.com/css2?family=Lexend:wght@600&family=Raleway:wght@300&family=Montserrat:wght@700&display=swap">
<style>
  :root {
    --ink: #000000;
    --paper: #ffffff;
    --backdrop: #ffffff;
  }
  * { margin: 0; padding: 0; box-sizing: border-box; }
  html, body {
    width: 886px;
    height: 1200px;
    overflow: hidden;
    background: var(--backdrop);
  }
  .cover {
    position: relative;
    width: 886px;
    height: 1200px;
    background: var(--paper);
  }
  .frame-outer {
    position: absolute;
    left: 22px; top: 22px; right: 22px; bottom: 22px;
    border: 9px solid var(--ink);
  }
  .frame-inner {
    position: absolute;
    left: 37px; top: 37px; right: 37px; bottom: 37px;
    border: 2px solid var(--ink);
  }
  .title {
    position: absolute;
    left: 0; right: 0;
    text-align: center;
    font-family: "Lexend", sans-serif;
    font-weight: 600;
    color: var(--ink);
    line-height: 1;
    letter-spacing: 2px;
    text-transform: uppercase;
  }
  .title-rise  { top: 158px; font-size: 172px; }
  .title-hum   { top: 360px; font-size: 132px; }
  .title-march { top: 633px; font-size: 168px; }
  .title-rest  { top: 814px; font-size: 132px; }
  .subtitle {
    position: absolute;
    left: 168px;
    top: 1016px;
    font-family: "Raleway", sans-serif;
    font-weight: 300;
    font-size: 42px;
    line-height: 1;
    color: var(--ink);
    text-transform: uppercase;
    white-space: nowrap;
  }
  .author {
    position: absolute;
    left: 230px;
    top: 1086px;
    font-family: "Montserrat", sans-serif;
    font-weight: 700;
    font-size: 42px;
    line-height: 1;
    color: var(--ink);
    text-transform: uppercase;
    white-space: nowrap;
  }
</style>
</head>
<body>
  <main class="cover">
    <div class="frame-outer"></div>
    <div class="frame-inner"></div>
    <h1>
      <span class="title title-rise">Rise</span>
      <span class="title title-hum">Hum</span>
      <span class="title title-march">March</span>
      <span class="title title-rest">Rest</span>
    </h1>
    <p class="subtitle">Music for the bagpipes</p>
    <p class="author">By Dermot Fairley</p>
  </main>
</body>
</html>
```